Letterhead Design Project

I need a letterhead design that uses the same design ideas as my business card, which I have attached. I need it to look professional but also fresh and clean. If possible I would also like a with compliments slip and envelope designed as well.

I have attached a copy of a sample word doc for the letterhead that shows everything that must be on it. I would also like an alternative with all of the information in the header. The with compliments slip must also have the same information on it.
With regards to the envelope I only really need the logo and my po box address.

Target Market(s)

30+ Professionals

Industry/Entity Type

Business

Requirements
Must have
• I have attached a copy of a sample word doc for the letterhead that shows everything that must be on it. I would also like an alternative with all of the information in the header. The with compliments slip must also have the same information on it.
Should not have
• I am not looking for anything with traditional text as I can do that myself. I am looking for something that will stand out from the crowd.

```html
<!DOCTYPE html>
<html lang="en">
<head>
<meta charset="utf-8">
<title>Harlow Insurance – Letterhead and Envelope</title>
<link href="https://fonts.googleapis.com/css2?family=Open+Sans:wght@400;600;700&display=swap" rel="stylesheet">
<style>
  :root {
    --brand-red: #e31b23;
    --ink: #3a3a3a;
    --ink-soft: #6b6b6b;
    --paper: #ffffff;
    --backdrop: #e4e4e4;
    --window-line: #9a9a9a;
    --window-fill: #f4f4f4;
    --sheet-shadow: rgba(0, 0, 0, 0.28);
  }
  * { margin: 0; padding: 0; box-sizing: border-box; }
  html, body {
    width: 1200px; height: 900px; overflow: hidden;
    background: var(--backdrop);
    font-family: "Open Sans", Arial, sans-serif;
    color: var(--ink);
  }
  .stage { position: relative; width: 1200px; height: 900px; }

  .sheet {
    position: absolute; background: var(--paper); overflow: hidden;
    box-shadow: 4px 5px 12px var(--sheet-shadow);
  }

  .brand { position: absolute; display: flex; align-items: center; gap: 7px; white-space: nowrap; }
  .brand-dot { width: 11px; height: 11px; border-radius: 50%; background: var(--brand-red); flex: none; }
  .brand-name { font-weight: 700; color: var(--brand-red); font-size: 14px; line-height: 1; }
  .brand-tagline { position: absolute; font-size: 6px; color: var(--ink-soft); white-space: nowrap; }

  .swoosh { position: absolute; top: 0; }

  /* Letterhead */
  .letterhead { left: 131px; top: 103px; width: 488px; height: 638px; z-index: 1; }
  .letterhead .brand { left: 22px; top: 28px; }
  .letterhead .brand-tagline { left: 40px; top: 46px; }
  .letterhead .swoosh { left: 100px; width: 110px; height: 95px; }
  .contact-block { position: absolute; top: 22px; font-size: 7px; line-height: 11px; color: var(--ink); white-space: nowrap; }
  .contact-block.address { left: 222px; }
  .contact-block.channels { left: 342px; }
  .contact-block .accent { color: var(--brand-red); font-weight: 600; margin-right: 3px; }
  .footer-band {
    position: absolute; left: 0; bottom: 0; width: 100%; height: 34px;
    background: var(--brand-red); color: var(--paper);
    font-size: 6px; line-height: 10px; text-align: right;
    padding: 7px 70px 0 0; white-space: nowrap;
  }
  .footer-band strong { font-weight: 700; }

  /* Envelope */
  .envelope { left: 497px; top: 431px; width: 531px; height: 250px; z-index: 2; }
  .envelope .brand { left: 26px; top: 28px; }
  .envelope .brand-tagline { left: 44px; top: 46px; }
  .envelope .swoosh { left: 160px; width: 90px; height: 78px; }
  .return-address { position: absolute; left: 26px; top: 68px; font-size: 7px; color: var(--ink); white-space: nowrap; }
  .address-window {
    position: absolute; left: 319px; top: 150px; width: 178px; height: 66px;
    border: 1.5px solid var(--window-line); border-radius: 3px;
    background: var(--window-fill);
  }
</style>
</head>
<body>
<main class="stage">

  <section class="sheet letterhead" aria-label="Letterhead">
    <div class="brand">
      <span class="brand-dot"></span>
      <span class="brand-name">Harlow Insurance</span>
    </div>
    <div class="brand-tagline">Cover that works for local business</div>

    <svg class="swoosh" viewBox="0 0 110 95" aria-hidden="true">
      <path d="M92 0 H106 C106 50 70 85 6 95 C50 78 88 48 92 0 Z" fill="var(--brand-red)"/>
    </svg>

    <div class="contact-block address">
      Unit 4, 18 Parkside Road<br>
      Eastwood SA 5071<br>
      PO Box 218, Eastwood SA 5071
    </div>
    <div class="contact-block channels">
      <span class="accent">T</span>08 8123 4567<br>
      <span class="accent">F</span>08 8123 4568<br>
      <span class="accent">E</span>info@harlowinsurance.com.au<br>
      <span class="accent">W</span>www.harlowinsurance.com.au
    </div>

    <footer class="footer-band">
      <strong>Harlow Insurance Brokers Pty Ltd</strong> ABN 12 345 678 901 AFS Licence 234567 | Authorised Representative<br>
      Harlow Insurance Group Pty Ltd ABN 98 765 432 109 AR 345678 | Corporate Authorised Representative
    </footer>
  </section>

  <section class="sheet envelope" aria-label="Envelope">
    <div class="brand">
      <span class="brand-dot"></span>
      <span class="brand-name">Harlow Insurance</span>
    </div>
    <div class="brand-tagline">Cover that works for local business</div>

    <svg class="swoosh" viewBox="0 0 110 95" aria-hidden="true">
      <path d="M92 0 H106 C106 50 70 85 6 95 C50 78 88 48 92 0 Z" fill="var(--brand-red)"/>
    </svg>

    <p class="return-address">PO Box 218, Eastwood SA 5071</p>
    <div class="address-window"></div>
  </section>

</main>
</body>
</html>
```